Outstanding but small benefit administration firm serving large clients needs a website redesign

While the content on our current website is fine, when people arrive at our website, they know immediately that it was designed years ago. We are looking for something that can potentially be maintained on a content management system because we would like to hire a google certified expert to help with adwords and they often want to change the website or add meta data. We want the design to be mobile device friendly.

As for our company, we stress data accuracy, client customization and outstanding customer service. All of our competitors are large corporations (Corvellan, Tolbin, Qualix, PerkWaypoint, etc.). When we get a client, they stay with us. So many of our competitors do a horrible job with administration that many companies just think that's the way it is in this industry. We need to change that thinking! There is someone who can do it right at a reasonable price. We have very few out of scope fees. RMT knows how to make the transition from one administrator to us as painless as possible.

We like our current colors. We don't have a lot of time to write additional content.

Target Market(s)

Companies with 5,000 to 50,000 employees

Coding

Coded - Design and coding required

Number of Pages Required

2 page

Font styles to use
Sans Serif

Requirements
Must have
• If everything doesn't fit on one page, please show me what the second page would look like. For example, if there are See More links, what happens?
• We need for people to be able to submit short contact us with their company name as a required field.
• Ideally this website will be put on wordpress or something similar.
• Must be mobile device friendly.
Should not have
• Login, Register, Maps of our location, website search

```html
<!DOCTYPE html>
<html lang="en">
<head>
<meta charset="utf-8">
<title>Reliant Member Trust</title>
<link rel="stylesheet" href="https://fonts.googleapis.com/css2?family=Source+Sans+3:wght@300;400;600&family=Arimo:wght@400&display=swap">
<style>
:root{
  --green-top:#6cc04a;
  --green-bottom:#3d9a25;
  --navy:#003a6e;
  --navy-deep:#002a50;
  --footer-top:#0c4a86;
  --footer-bottom:#002c55;
  --grey-band:#b2b2b2;
  --card-bg:#f2f2f2;
  --card-border:#c8c8c8;
  --rule:#dcdcdc;
  --body-text:#444;
  --logo-text:#7a7a7a;
  --pill:#8c8c8c;
  --white:#fff;
}
*{box-sizing:border-box;margin:0;padding:0}
html,body{width:999px;height:1200px;overflow:hidden;background:var(--white)}
body{position:relative;font-family:"Source Sans 3",sans-serif;color:var(--body-text)}
.abs{position:absolute}
a{color:inherit;text-decoration:none}

/* header */
.site-header{left:0;top:0;width:999px;height:110px;background:var(--white)}
.brand{left:22px;top:38px;display:flex;align-items:center;gap:14px}
.brand-dot{width:36px;height:36px;border-radius:50%;background:#7cc242}
.brand-name{font-size:31px;font-weight:400;color:var(--logo-text);letter-spacing:.3px;line-height:36px}

/* nav */
.main-nav{left:0;top:110px;width:999px;height:28px;background:linear-gradient(var(--green-top),var(--green-bottom))}
.nav-item{top:0;height:28px;display:flex;align-items:center;justify-content:center;font-family:"Arimo",sans-serif;font-size:12px;color:var(--white);width:90px}
.nav-item.is-active{background:var(--navy)}

/* hero */
.hero{left:0;top:138px;width:999px;height:373px}
.hero-photo{left:0;top:0;width:999px;height:373px;background:linear-gradient(90deg,#c9d9e6 0%,#a9c1d4 35%,#4b5f72 60%,#1f2a36 100%)}
.hero-panel{left:593px;top:37px;width:406px;height:211px;background:rgba(160,190,220,.55)}
.hero-title{right:21px;top:44px;text-align:right;font-size:40px;font-weight:300;line-height:1.05;color:var(--white)}
.hero-rule{left:706px;top:155px;width:278px;height:1px;background:#7fcf4e}
.hero-text{right:21px;top:168px;width:340px;text-align:right;font-size:17px;line-height:21.5px;color:var(--white)}
.btn{display:flex;align-items:center;justify-content:center;border-radius:10px;color:var(--white);font-size:15px;border:0;font-family:inherit}
.btn-green{background:linear-gradient(var(--green-top),var(--green-bottom))}
.btn-navy{background:linear-gradient(#0d4f8c,var(--navy-deep))}
.btn-learn{left:751px;top:257px;width:108px;height:36px}
.btn-serv{left:869px;top:257px;width:109px;height:36px}

/* contact band */
.band-navy{left:0;top:511px;width:999px;height:69px;background:linear-gradient(90deg,#0a3a6c,#074282)}
.contact-form{left:20px;top:19px;display:flex;gap:12px;align-items:center}
.contact-form input{height:31px;border:0;border-radius:4px;padding:0 10px;font-family:"Arimo",sans-serif;font-size:13px;color:#333;background:var(--white)}
.contact-form .field{width:168px}
.contact-form .field-msg{width:262px}
.contact-form .btn-send{width:96px;height:31px;font-size:15px;border-radius:8px}
.band-grey{left:0;top:580px;width:999px;height:28px;background:var(--grey-band)}

/* service cards */
.card{top:648px;width:314px;height:289px;background:var(--card-bg);border:1px solid var(--card-border)}
.card-title{position:absolute;left:11px;top:8px;width:290px;height:42px;background:linear-gradient(var(--green-top),var(--green-bottom));color:var(--white);font-size:23px;font-weight:400;display:flex;align-items:center;justify-content:center}
.card-rule{position:absolute;left:14px;width:286px;height:1px;background:var(--rule)}
.card-photo{position:absolute;left:11px;top:83px;width:138px;height:129px}
.card-text{position:absolute;left:159px;top:80px;width:140px;font-size:13.5px;line-height:16.8px;color:var(--body-text)}
.card-btn{position:absolute;left:95px;top:244px;width:125px;height:26px;border-radius:13px;background:var(--pill);color:var(--white);font-family:"Arimo",sans-serif;font-size:11px;display:flex;align-items:center;justify-content:center}

/* footer */
.site-footer{left:0;top:974px;width:999px;height:176px;background:linear-gradient(var(--footer-top),var(--footer-bottom))}
.footer-col{top:30px;width:200px;color:var(--white)}
.footer-col h3{font-weight:400;font-size:20px;padding-bottom:8px;border-bottom:1px solid #5c8fc0;width:169px;margin-bottom:13px}
.footer-col a{display:block;font-family:"Arimo",sans-serif;font-size:14px;line-height:26.5px}
.footer-bar{left:0;top:1150px;width:999px;height:50px;background:#000}
.bar-links{left:315px;top:0;height:50px;display:flex;align-items:center;font-family:"Arimo",sans-serif;font-size:12px;color:#bbb}
.bar-links span.sep{margin:0 40px;color:#888}
.social{top:12px;width:26px;height:26px;border-radius:50%;background:#8a8a8a}
</style>
</head>
<body>

<header class="site-header abs">
  <div class="brand abs"><span class="brand-dot"></span><span class="brand-name">Reliant Member Trust</span></div>
</header>

<nav class="main-nav abs">
  <a class="nav-item is-active abs" style="left:225px" href="#">HOME</a>
  <a class="nav-item abs" style="left:372px" href="#">ABOUT</a>
  <a class="nav-item abs" style="left:523px" href="#">REVIEWS</a>
  <a class="nav-item abs" style="left:675px" href="#">CONTACT</a>
</nav>

<section class="hero abs">
  <div class="hero-photo abs" role="img" aria-label="Businessman pointing at a cloud of floating portrait tiles of professionals"></div>
  <div class="hero-panel abs"></div>
  <h1 class="hero-title abs">Reliant Member<br>Trust (RMT)</h1>
  <div class="hero-rule abs"></div>
  <p class="hero-text abs">Is a boutique organization providing large plan sponsors with a customer service model using only trained benefit professionals...</p>
  <a class="btn btn-green btn-learn abs" href="#">Learn More</a>
  <a class="btn btn-navy btn-serv abs" href="#">View Serives</a>
</section>

<div class="band-navy abs">
  <form class="contact-form abs" action="#" method="post" aria-label="Quick contact">
    <input class="field" type="text" name="name" placeholder="Your name" aria-label="Your name">
    <input class="field" type="text" name="company" placeholder="Company name *" aria-label="Company name" required>
    <input class="field" type="email" name="email" placeholder="Email address" aria-label="Email address">
    <input class="field-msg" type="text" name="message" placeholder="Short message" aria-label="Short message">
    <button class="btn btn-green btn-send" type="submit">Send</button>
  </form>
</div>
<div class="band-grey abs"></div>

<article class="card abs" style="left:17px">
  <h2 class="card-title">Health Administration</h2>
  <div class="card-rule" style="top:60px"></div>
  <div class="card-photo" role="img" aria-label="Doctor with stethoscope in a hospital corridor" style="background:linear-gradient(135deg,#e8e4df,#b9c9d4)"></div>
  <p class="card-text">lorem ipsum dolor sit amet consectetur und adipiscing elit sit amet lorem ipsum dolor sit amet consectetur und elit sit amet ipsum sit elit. ipsum lorem</p>
  <div class="card-rule" style="top:228px"></div>
  <a class="card-btn" href="#">VIEW DETAILS</a>
</article>

<article class="card abs" style="left:342px">
  <h2 class="card-title">Benefit Administration</h2>
  <div class="card-rule" style="top:60px"></div>
  <div class="card-photo" role="img" aria-label="Brick office building under a cloudy sky" style="background:linear-gradient(#c8d6e4 0%,#b9c6d2 40%,#9a6a4c 60%,#8f8f8f 100%)"></div>
  <p class="card-text">lorem ipsum dolor sit amet consectetur und adipiscing elit sit amet lorem ipsum dolor sit amet consectetur und adipiscing elit sit amet sit consectetur elit.</p>
  <div class="card-rule" style="top:228px"></div>
  <a class="card-btn" href="#">VIEW DETAILS</a>
</article>

<article class="card abs" style="left:666px">
  <h2 class="card-title">Benefit Consulting</h2>
  <div class="card-rule" style="top:60px"></div>
  <div class="card-photo" role="img" aria-label="Modern glass-fronted office entrance with landscaped garden" style="background:linear-gradient(#aac8e6 0%,#c7ccd2 45%,#6f7d86 70%,#6c7a48 100%)"></div>
  <p class="card-text">lorem ipsum dolor sit amet consectetur und adipiscing elit sit amet lorem ipsum dolor und adipiscing elit sit amet lorem adipiscing sit consectetur.</p>
  <div class="card-rule" style="top:228px"></div>
  <a class="card-btn" href="#">VIEW DETAILS</a>
</article>

<footer class="site-footer abs">
  <div class="footer-col abs" style="left:66px">
    <h3>About Us</h3>
    <a href="#">General Information</a>
    <a href="#">Our Mission</a>
  </div>
  <div class="footer-col abs" style="left:306px">
    <h3>Customer Reviews</h3>
    <a href="#">Adipiscing Elit</a>
    <a href="#">Ipsum Lorem Sit Amet</a>
  </div>
  <div class="footer-col abs" style="left:546px">
    <h3>Our Services</h3>
    <a href="#">Lorem ipsum</a>
    <a href="#">Dolor Sit Amet Consectetur</a>
  </div>
  <div class="footer-col abs" style="left:796px">
    <h3>Contact Us</h3>
    <a href="#">Socialine</a>
    <a href="#">Chirper</a>
    <a href="#">Email us</a>
  </div>
</footer>

<div class="footer-bar abs">
  <div class="bar-links abs">
    <a href="#">HOME</a><span class="sep">|</span>
    <a href="#">ABOUT</a><span class="sep">|</span>
    <a href="#">REVIEWS</a><span class="sep">|</span>
    <a href="#">CONTACT</a>
  </div>
  <span class="social abs" style="left:838px"></span>
  <span class="social abs" style="left:889px"></span>
  <span class="social abs" style="left:941px"></span>
</div>

</body>
</html>
```